Letterhead for Dorian Welk

I need a letterhead based on the business card design

Industry/Entity Type

Business

Requirements
Must have
• Footer: Dorian Welk Naturopath
Shop 4123c, 46 Carrow Lane, Sydney 2000

```html
<!DOCTYPE html>
<html lang="en">
<head>
<meta charset="utf-8">
<title>Dorian Welk Naturopath – Letterhead</title>
<link href="https://fonts.googleapis.com/css2?family=Montserrat:wght@500&family=Quicksand:wght@500;700&display=swap" rel="stylesheet">
<style>
  :root {
    --backdrop: #e9e7e4;
    --paper: #ffffff;
    --brand-orange: #f7901e;
    --leaf-tint: #fbe0c6;
    --leaf-tint-soft: rgba(251, 224, 198, 0);
    --footer-text: #ffffff;
  }
  html, body {
    margin: 0;
    padding: 0;
    width: 1200px;
    height: 1000px;
    overflow: hidden;
    background: var(--backdrop);
  }
  .letterhead {
    position: absolute;
    left: 310px;
    top: 95px;
    width: 579px;
    height: 818px;
    background: var(--paper);
    overflow: hidden;
    box-shadow: 0 2px 10px rgba(0,0,0,0.12);
  }
  .brand {
    position: absolute;
    left: 60px;
    top: 55px;
    display: flex;
    align-items: center;
    gap: 8px;
  }
  .brand-dot {
    width: 10px;
    height: 10px;
    border-radius: 50%;
    background: var(--brand-orange);
  }
  .brand-name {
    font-family: "Montserrat", sans-serif;
    font-weight: 500;
    font-size: 21px;
    letter-spacing: 0.5px;
    color: var(--brand-orange);
    text-transform: uppercase;
    margin: 0;
  }
  .foliage {
    position: absolute;
    bottom: 27px;
    background: linear-gradient(to top, var(--leaf-tint) 0%, var(--leaf-tint) 55%, var(--leaf-tint-soft) 100%);
  }
  .foliage--left {
    left: 2px;
    width: 213px;
    height: 590px;
    border-radius: 0 120px 60px 0;
  }
  .foliage--right {
    right: 0;
    width: 221px;
    height: 545px;
    border-radius: 120px 0 0 60px;
  }
  .footer-band {
    position: absolute;
    left: 0;
    bottom: 0;
    width: 100%;
    height: 27px;
    background: var(--brand-orange);
    display: flex;
    align-items: center;
    justify-content: center;
    font-family: "Quicksand", sans-serif;
    font-weight: 500;
    font-size: 8.5px;
    color: var(--footer-text);
    white-space: nowrap;
  }
  .footer-band .sep {
    margin: 0 14px;
  }
  .footer-band .footer-name {
    font-weight: 700;
  }
</style>
</head>
<body>
  <main class="letterhead">
    <header class="brand">
      <span class="brand-dot"></span>
      <h1 class="brand-name">Dorian Welk</h1>
    </header>

    <div class="foliage foliage--left" role="img" aria-label="Soft translucent peach leaf illustration rising along the left edge"></div>
    <div class="foliage foliage--right" role="img" aria-label="Soft translucent peach leaf illustration rising along the right edge"></div>

    <footer class="footer-band">
      <span class="footer-name">Dorian Welk Naturopath</span>
      <span class="sep">|</span>
      <span>Shop 4123c, 46 Carrow Lane, Sydney 2000</span>
      <span class="sep">|</span>
      <span>dwnaturopath@mailbox.com</span>
      <span class="sep">|</span>
      <span>P.0400 555 318</span>
    </footer>
  </main>
</body>
</html>
```